Red Sea Boat trips in need of Business Card for Private Boat Tours

We need a Business card for a new business set-up in Egypt on the Red Sea for private snorkelling and boat excursions to one of the world's most beautiful reefs. We have wording logo already set-up which matches the boat but we need business cards to be bright and colourful with pictures of boat

Industry/Entity Type

Tourism

Contact Information for Business Card

Two Silver Herons (font provided) Boat Trips

```html
<!DOCTYPE html>
<html lang="de">
<head>
<meta charset="utf-8">
<title>Two Silver Herons – Business Card</title>
<link rel="stylesheet" href="https://fonts.googleapis.com/css2?family=Roboto+Condensed:wght@400;500;700;800&display=swap">
<style>
  :root {
    --stage: #6e6e6e;
    --harbour-dark: #2a3338;
    --cockpit-grey: #8e9aa3;
    --windshield: #8cc3c6;
    --deck-white: #e9ebee;
    --deck-light: #d6d9de;
    --deck-mid: #b3b8c0;
    --ink: #0d0d0d;
    --reef-orange: #a8552c;
    --reef-brown: #5e4a3a;
    --sea-blue: #1d4f7a;
    --sea-deep: #0c2540;
    --card-black: #050608;
    --name-blue: #5b7fd1;
    --rule-blue: #6b8fd8;
    --text-light: #f2f2f2;
  }
  * { box-sizing: border-box; margin: 0; padding: 0; }
  html, body {
    width: 1200px; height: 900px; overflow: hidden;
    background: var(--stage);
    font-family: "Roboto Condensed", sans-serif;
  }
  .card {
    position: absolute;
    top: 150px;
    width: 386px; height: 600px;
    border-radius: 21px;
    overflow: hidden;
  }
  .card--front { left: 199px; }
  .card--back { left: 636px; }

  .boat-photo {
    position: absolute; inset: 0;
    background:
      radial-gradient(ellipse 30% 22% at 50% 82%, rgba(40,45,52,0.55) 0%, rgba(40,45,52,0) 100%),
      linear-gradient(90deg, rgba(42,51,56,0.55) 0%, rgba(42,51,56,0) 8%, rgba(42,51,56,0) 92%, rgba(42,51,56,0.55) 100%),
      linear-gradient(180deg,
        var(--harbour-dark) 0%,
        var(--cockpit-grey) 7%,
        var(--windshield) 18%,
        var(--windshield) 26%,
        var(--deck-white) 33%,
        var(--deck-light) 55%,
        var(--deck-white) 75%,
        var(--deck-mid) 100%);
  }
  .brand-name {
    position: absolute; left: 0; right: 0; top: 244px;
    text-align: center;
    font-weight: 800; font-size: 48px; line-height: 60px;
    color: var(--ink);
    white-space: nowrap;
  }

  .reef-photo {
    position: absolute; inset: 0;
    background:
      linear-gradient(180deg, rgba(5,6,8,0) 0%, rgba(5,6,8,0) 48%, rgba(5,6,8,0.75) 68%, var(--card-black) 88%),
      radial-gradient(ellipse 55% 45% at 20% 30%, var(--reef-orange) 0%, var(--reef-brown) 45%, rgba(94,74,58,0) 80%),
      linear-gradient(180deg, var(--sea-blue) 0%, var(--sea-deep) 70%);
  }
  .contact {
    position: absolute; left: 33px; top: 0; right: 20px;
    color: var(--text-light);
  }
  .contact__name {
    position: absolute; top: 342px; left: 0;
    font-weight: 700; font-size: 31px; color: var(--name-blue);
    white-space: nowrap;
  }
  .contact__role {
    position: absolute; top: 381px; left: 0;
    font-weight: 500; font-size: 18px; white-space: nowrap;
  }
  .contact__rule {
    position: absolute; top: 416px; left: 0;
    width: 252px; height: 1px; background: var(--rule-blue);
  }
  .contact__line {
    position: absolute; left: 0;
    display: flex; align-items: center; gap: 6px;
    font-size: 17px; font-weight: 500; white-space: nowrap;
    letter-spacing: 0.4px;
  }
  .contact__line svg { width: 13px; height: 13px; flex: none; fill: var(--text-light); }
  .contact__line .indent { padding-left: 19px; }
  .line-street { top: 430px; }
  .line-city { top: 455px; }
  .line-phone { top: 491px; letter-spacing: 2px; }
  .line-mail { top: 517px; }
  .line-web { top: 544px; }
</style>
</head>
<body>
  <section class="card card--front">
    <div class="boat-photo" role="img" aria-label="Photo of a white motor boat bow with quilted grey sun-deck cushions, windshield and deck hatch, seen from above"></div>
    <div class="brand-name">Two Silver Herons</div>
  </section>

  <section class="card card--back">
    <div class="reef-photo" role="img" aria-label="Underwater photo of a coral reef with orange fish and a scuba diver in deep blue water"></div>
    <div class="contact">
      <div class="contact__name">Lukas Reinhardt</div>
      <div class="contact__role">Geschäftsführender/Gesellschafter</div>
      <div class="contact__rule"></div>

      <div class="contact__line line-street">
        <svg viewBox="0 0 24 24"><path d="M12 1C7.6 1 4 4.6 4 9c0 6 8 14 8 14s8-8 8-14c0-4.4-3.6-8-8-8zm0 11a3 3 0 1 1 0-6 3 3 0 0 1 0 6z"/></svg>
        <span>Lindenweg 12</span>
      </div>
      <div class="contact__line line-city"><span class="indent">10115 Berlin</span></div>

      <div class="contact__line line-phone">
        <svg viewBox="0 0 24 24"><path d="M6.6 10.8a15.1 15.1 0 0 0 6.6 6.6l2.2-2.2c.3-.3.7-.4 1-.2 1.1.4 2.3.6 3.6.6.6 0 1 .4 1 1V20c0 .6-.4 1-1 1C10.6 21 3 13.4 3 4c0-.6.4-1 1-1h3.5c.6 0 1 .4 1 1 0 1.3.2 2.5.6 3.6.1.3 0 .7-.2 1z"/></svg>
        <span>+49 170 5550142</span>
      </div>
      <div class="contact__line line-mail">
        <svg viewBox="0 0 24 24"><path d="M2 5h20v14H2z M2 5l10 8 10-8" fill="none" stroke="#f2f2f2" stroke-width="2"/></svg>
        <span>l.reinhardt@seaventure.de</span>
      </div>
      <div class="contact__line line-web">
        <svg viewBox="0 0 24 24"><g fill="none" stroke="#f2f2f2" stroke-width="1.8"><circle cx="12" cy="12" r="10"/><ellipse cx="12" cy="12" rx="4.5" ry="10"/><path d="M2 12h20M4 6.5h16M4 17.5h16"/></g></svg>
        <span>www.seaventure.de</span>
      </div>
    </div>
  </section>
</body>
</html>
```